Professional Engineering Web Design

Project Brief: Website Redesign for Mechanical Design Consultancy
Project Overview
I want to update and improve my current website to create a more professional, modern, and high-credibility online presence for my mechanical design consultancy.

Current site: https://valtrobuild.design/

The new website must communicate expertise, precision, and trust—matching the standard of top engineering and product design agencies.

Reference Websites (Style + Structure Inspiration)
These represent the quality, cleanliness, and professionalism I want to achieve:

https://plinthformworks.com/
https://www.zorvanta.com/
https://quellory-uk.com/
Brand Look
Professional, modern, engineering-focused aesthetic
Clean layouts and strong typography
High-quality imagery conveying precision, innovation, and mechanical expertise
Colour scheme and styling must follow my existing logo (attached in project)
Platform Requirements
The website must be built on WordPress
Should use a clean, flexible theme or modern page builder (Elementor, Gutenberg, Bricks, or similar)
Avoid overly complex custom coding so I can easily edit content later
Final deliverable must allow me to manage and update content without developer assistance
Functionality
Fast-loading, lightweight, and smooth user experience
Clean animations and transitions similar to the reference sites
Fully mobile responsive
Clear navigation and strong visual hierarchy
Contact forms optimised for lead generation
Optional: subtle scroll effects, case study sliders, icon animations, etc.
SEO Aspirations
Developer should recommend and implement a modern SEO strategy
Proper on-page SEO setup (titles, meta, schema, alt tags, heading structure)
Optimised site architecture for ranking and crawling
Aim: Generate leads through improved visibility and keyword targeting
Optional but useful: Google Analytics, Google Search Console setup
User Journeys
(Recommended structure)

The site should be crafted around clear, intuitive journeys for each type of visitor:

Potential new clients
Quickly understand what services I offer
View examples of past work / case studies
See credibility indicators (process, expertise, industries served)
Easily contact me or request a project discussion
Returning clients
Access updated portfolio items
Find contact details or book follow-up work easily
General visitors discovering through SEO
Be guided to valtro service areas
Understand my value proposition quickly
Be invited to learn more or make contact
The developer should design the structure to support these journeys smoothly.

Maintenance Expectations
Website will be maintained by me, so it should be easy to update using relatively basic WordPress skills
Use modular templates and simple backend structure
Avoid unnecessary plugins
Provide brief handover documentation if required
Hosting Preferences
Site is currently hosted via a family member
Open to discussing moving to a paid, reliable hosting provider if preferable for performance and maintainability
Developer may advise on the best hosting setup for WordPress
Content
Most content can be taken from the existing website
Developer is welcome to suggest improvements to structure, layout, and imagery
Must remain easy for me to edit or add new content later (e.g., new projects)
Deliverables
Fully built WordPress website
Clean, professional, modern design inspired by the reference sites
Mobile-responsive across all devices
SEO-ready structure and optimisations
Transfer of website and admin rights
Any design assets, templates, or documentation used

```html
<!DOCTYPE html>
<html lang="en">
<head>
<meta charset="utf-8">
<title>Valtro Mechanical Design — Mechanical CAD Design</title>
<link href="https://fonts.googleapis.com/css2?family=Inter:ital,wght@0,300;0,400;0,500;0,600;1,400&family=Poppins:wght@600&display=swap" rel="stylesheet">
<style>
:root{
  --blue:#3158f0;
  --blue-soft:#b9c6fa;
  --ink:#1f2330;
  --muted:#5d6270;
  --panel:#f0f1f4;
  --line:#d9dbe1;
  --dark:#3a3a3c;
  --white:#ffffff;
}
*{box-sizing:border-box;margin:0;padding:0}
html,body{width:1200px;height:4121px;overflow:hidden;background:var(--white)}
body{position:relative;font-family:"Inter",sans-serif;color:var(--ink)}
.abs{position:absolute}
.photo{position:absolute;overflow:hidden}

/* header */
.hero-panel{left:0;top:0;width:1200px;height:1293px;background:var(--panel);border-radius:0 0 128px 128px}
.logo{left:90px;top:29px;display:flex;align-items:center;gap:14px}
.logo-dot{width:54px;height:54px;border-radius:50%;background:var(--blue)}
.logo-name{font-size:36px;font-weight:500;letter-spacing:6px;color:var(--ink);line-height:1}
.logo-tag{font-size:9px;font-weight:600;letter-spacing:1.4px;color:var(--blue);margin-top:4px}
.nav{left:422px;top:38px;width:356px;height:37px;border:1px solid var(--line);border-radius:20px;background:var(--white);display:flex;align-items:center;padding:0 4px;gap:2px;font-size:11px;color:var(--ink);white-space:nowrap}
.nav a{text-decoration:none;color:inherit;padding:8px 9px;border-radius:16px;white-space:nowrap;line-height:1}
.nav .active{background:var(--blue);color:var(--white);padding:9px 19px;margin-right:6px}
.nav .search{margin-left:auto;width:28px;height:28px;border-radius:50%;background:var(--dark);display:flex;align-items:center;justify-content:center;flex:none}
.call{left:960px;top:40px;display:flex;align-items:center;gap:10px;font-size:11px;line-height:1.3}
.call-ico{width:34px;height:34px;border-radius:50%;background:var(--blue);display:flex;align-items:center;justify-content:center}
.call b{font-weight:600}

/* hero */
.hero-title{left:0;width:1200px;top:188px;text-align:center;font-size:48px;font-weight:400;letter-spacing:-.6px;line-height:1.15}
.hero-title .title-text{position:relative;display:inline-block}
.hero-title small{position:absolute;left:100%;margin-left:8px;top:16px;font-size:10px;color:var(--blue);text-align:left;line-height:1.25;letter-spacing:0;white-space:nowrap}
.hero-intro{left:280px;width:640px;top:265px;text-align:center;font-size:12px;line-height:1.6;color:var(--muted)}
.hero-photo{left:216px;top:331px;width:768px;height:397px;border-radius:48px;background:linear-gradient(135deg,#3f4750,#6f7884 45%,#2d3a4a)}

/* expertise */
.section-title{left:0;width:1200px;text-align:center;font-size:42px;font-weight:400;letter-spacing:-.4px}
.card{top:888px;width:288px;height:312px;border:1.5px solid #cfd2d9;border-radius:22px;background:var(--white);text-align:center}
.card svg{margin-top:30px}
.card h3{font-size:15px;font-weight:400;margin-top:10px}
.card p{font-size:11px;color:var(--muted);line-height:1.6;margin:10px 22px 0}
.card .photo{left:13px;top:176px;width:262px;height:120px;border-radius:16px}

/* about */
.eyebrow{left:0;width:1200px;text-align:center;font-size:14px}
.about-photo{left:173px;top:1466px;width:392px;height:182px;border-radius:22px;background:linear-gradient(120deg,#6a7b8c,#3b4a5a 60%,#8a8f95)}
.about-text{left:621px;top:1505px;width:410px;font-size:12.5px;font-style:italic;line-height:1.6;color:var(--muted)}
.divider{left:138px;top:1714px;width:923px;height:1px;background:var(--line)}

/* services */
.services-title{left:256px;top:1778px;font-size:42px;font-weight:400}
.services-sub{left:661px;top:1800px;font-size:14px;color:var(--muted)}
.marquee{left:-258px;top:2034px;white-space:nowrap;font-size:45px;color:var(--blue-soft);letter-spacing:.5px}
.service-card{left:373px;top:1877px;width:454px;height:381px;background:var(--blue);border-radius:32px;box-shadow:0 20px 40px rgba(49,88,240,.25)}
.service-card .photo{left:11px;top:11px;width:432px;height:278px;border-radius:22px 22px 0 0;background:linear-gradient(135deg,#2c3c5c,#7d8ca6 50%,#3b4556)}
.service-card h3{position:absolute;left:40px;top:318px;font-size:27px;font-weight:400;color:var(--white)}
.service-arrow{position:absolute;left:370px;top:312px;width:48px;height:48px;border-radius:10px;background:var(--dark);display:flex;align-items:center;justify-content:center}

/* work */
.work-sub{left:0;width:1200px;top:2405px;text-align:center;font-size:15px;color:var(--muted)}
.work-photo{left:0;top:2458px;width:1200px;height:507px;border-radius:100px;background:linear-gradient(110deg,#5b6470,#2a323c 40%,#6b7684 70%,#c9c2ba)}
.work-card{left:22px;top:2483px;width:351px;height:455px;border-radius:44px;background:rgba(110,112,116,.88);border:1.5px solid rgba(255,255,255,.35);color:var(--white);padding:70px 44px 0}
.work-card h3{font-size:24px;font-weight:400;line-height:1.3}
.work-card p{font-size:11.5px;line-height:1.65;margin-top:14px}
.btn{display:inline-block;background:var(--blue);color:var(--white);font-size:11px;font-weight:500;border-radius:20px;text-decoration:none;text-align:center}
.work-card .btn{margin-top:20px;width:126px;height:33px;line-height:33px}

/* feedback */
.feedback-title{left:166px;top:3112px;font-size:32px;font-weight:400;line-height:1.3}
.feedback-btn{left:166px;top:3214px;width:229px;height:40px;line-height:40px}
.quote-mark{left:608px;top:3058px}
.quote-text{left:610px;top:3126px;width:425px;font-size:12.5px;font-style:italic;line-height:1.6;color:var(--muted)}
.quote-name{left:610px;top:3240px;font-size:14px}
.quote-name span{font-size:9px;color:var(--blue);margin-left:6px}

/* cta */
.cta{left:112px;top:3354px;width:976px;height:206px;border-radius:64px;background:var(--blue);text-align:center;color:var(--white)}
.cta h2{font-size:51px;font-weight:400;margin-top:40px;letter-spacing:-.3px}
.cta a{display:inline-block;margin-top:22px;width:106px;height:40px;line-height:40px;border-radius:20px;background:var(--white);color:var(--ink);font-size:11px;text-decoration:none}

/* footer */
.footer{left:0;top:3586px;width:1200px;height:535px;background:var(--dark);border-radius:128px 128px 0 0;color:var(--white)}
.social{position:absolute;top:62px;width:32px;height:32px;border-radius:50%;background:#4c4c50;border:1px solid #5c5c62}
.f-info{position:absolute;top:63px;font-size:15px;white-space:nowrap}
.f-info small{display:block;font-size:10px;color:#bdbdc2;margin-bottom:6px}
.f-bar{position:absolute;left:114px;top:144px;width:971px;height:78px;border:1.5px solid #77777c;border-radius:40px;font-size:14px}
.f-bar .top{position:absolute;left:58px;top:30px}
.f-bar .copy{position:absolute;left:609px;top:18px;line-height:1.4;white-space:nowrap}
.wordmark{position:absolute;left:0;top:230px;width:1200px;text-align:center;font-family:"Poppins",sans-serif;font-weight:600;font-size:250px;letter-spacing:18px;line-height:1;color:var(--white)}
</style>
</head>
<body>

<div class="abs hero-panel"></div>

<header>
  <div class="abs logo">
    <div class="logo-dot"></div>
    <div>
      <div class="logo-name">valtro</div>
      <div class="logo-tag">MECHANICAL DESIGN</div>
    </div>
  </div>
  <nav class="abs nav">
    <a class="active" href="#">Home</a>
    <a href="#">Portfolio</a>
    <a href="#">Our Services</a>
    <a href="#">Contact Us</a>
    <span class="search"><svg width="12" height="12" viewBox="0 0 12 12"><circle cx="5" cy="5" r="3.5" fill="none" stroke="#fff" stroke-width="1.4"/><line x1="7.6" y1="7.6" x2="10.5" y2="10.5" stroke="#fff" stroke-width="1.4"/></svg></span>
  </nav>
  <div class="abs call">
    <span class="call-ico"><svg width="16" height="16" viewBox="0 0 24 24"><path d="M6.6 10.8a15 15 0 0 0 6.6 6.6l2.2-2.2a1 1 0 0 1 1-.25 11.4 11.4 0 0 0 3.6.6 1 1 0 0 1 1 1V20a1 1 0 0 1-1 1A17 17 0 0 1 3 4a1 1 0 0 1 1-1h3.5a1 1 0 0 1 1 1c0 1.25.2 2.45.6 3.6a1 1 0 0 1-.25 1z" fill="#fff"/></svg></span>
    <div><b>Call Us</b><br>+44 (0)7700 900 318</div>
  </div>
</header>

<section>
  <h1 class="abs hero-title"><span class="title-text">Mechanical CAD Design<small>Cutting<br>Edge Engineering</small></span></h1>
  <p class="abs hero-intro">Welcome to Valtro Mechanical Design. We are a UK based design consultancy offering a comprehensive mechanical and product design service from initial concepts through to full volume production.</p>
  <div class="photo hero-photo" role="img" aria-label="Engineers working on CAD models across dual monitors in a design office"></div>
</section>

<section>
  <h2 class="abs section-title" style="top:800px">Our Expertise</h2>

  <div class="abs card" style="left:150px">
    <svg width="40" height="40" viewBox="0 0 40 40" fill="none" stroke="#3158f0" stroke-width="1.6"><path d="M6 30l8-6h10a3 3 0 0 1 0 6h-8"/><path d="M6 36l6-3h14l10-9"/><rect x="16" y="6" width="14" height="12" rx="2"/><path d="M20 10h6M20 14h4"/></svg>
    <h3>Bespoke Product Design</h3>
    <p>Innovative design from concept through the full development life cycle</p>
    <div class="photo" style="background:linear-gradient(135deg,#8f969d,#3c434b 60%,#b7bcc0)" role="img" aria-label="Concept appliance renders on a workstation screen"></div>
  </div>

  <div class="abs card" style="left:456px">
    <svg width="40" height="40" viewBox="0 0 40 40" fill="none" stroke="#3158f0" stroke-width="1.6"><rect x="5" y="6" width="30" height="21" rx="2"/><path d="M15 33h10M20 27v6"/><path d="M20 10l6 3.5v6L20 23l-6-3.5v-6z"/><path d="M14 13.5l6 3.5 6-3.5M20 17v6"/></svg>
    <h3>3D Modelling and Drawings</h3>
    <p>We create 3D CAD, 2D engineering drawings and photorealistic renders</p>
    <div class="photo" style="background:linear-gradient(135deg,#4a5ad8,#aeb4c4 55%,#6d7480)" role="img" aria-label="Engineer inspecting a machined metal part beside a 3D model"></div>
  </div>

  <div class="abs card" style="left:762px">
    <svg width="40" height="40" viewBox="0 0 40 40" fill="none" stroke="#3158f0" stroke-width="1.6"><rect x="6" y="22" width="28" height="12" rx="1"/><path d="M10 22V10h8v12M14 6v4"/><circle cx="28" cy="12" r="5"/><path d="M10 28h4M18 28h4M26 28h4"/></svg>
    <h3>Design for Manufacture</h3>
    <p>Creating designs optimised for prototype and production manufacture</p>
    <div class="photo" style="background:linear-gradient(135deg,#c9b79e,#7a7269 50%,#9aa4ae)" role="img" aria-label="CNC milling machine cutting a part while a tablet shows the design"></div>
  </div>
</section>

<section>
  <p class="abs eyebrow" style="top:1362px">About Us</p>
  <h2 class="abs section-title" style="top:1384px">Who We Are</h2>
  <div class="photo about-photo" role="img" aria-label="Engineering team reviewing designs on computers in a bright office"></div>
  <p class="abs about-text">Rowan Ellis is the Chief Engineer at Valtro Mechanical Design. He has 11 years experience working as a mechanical design engineer in multiple industries including high performance automotive, consumer products, medical, industrial plus many more. He has worked in multiple roles across a wide range of products.</p>
  <div class="abs divider"></div>
</section>

<section>
  <h2 class="abs services-title">Our Services</h2>
  <p class="abs services-sub">We offer a comprehensive design service</p>
  <div class="abs marquee">Project Management * Project Management * Project Management * Project Management</div>
  <div class="abs service-card">
    <div class="photo" role="img" aria-label="Team meeting around a table discussing project charts"></div>
    <h3>Project Management</h3>
    <span class="service-arrow"><svg width="20" height="20" viewBox="0 0 20 20" fill="none" stroke="#fff" stroke-width="1.6"><path d="M4 16L16 4M8 4h8v8"/></svg></span>
  </div>
</section>

<section>
  <h2 class="abs section-title" style="top:2346px">Our Work</h2>
  <p class="abs work-sub">A small selection of our previous projects</p>
  <div class="photo work-photo" role="img" aria-label="Engineer at a desk modelling transmission housings in CAD on two monitors"></div>
  <article class="abs work-card">
    <h3>Dual Clutch<br>Transmission Design</h3>
    <p>We worked alongside a large design team to design an 8 speed dual clutch transmission for a supercar.</p>
    <p>Our key focus areas were the cast housings. As you can see from the images these housings were highly complex and included a lot of functionality. Supporting hundreds of parts and very tightly toleranced, attention to detail and precision was key in this project.</p>
    <a class="btn" href="#">Learn More</a>
  </article>
</section>

<section>
  <h2 class="abs feedback-title">Feedback from some<br>of our recent customers</h2>
  <a class="abs btn feedback-btn" href="#">Read Our Client Success Stories</a>
  <svg class="abs quote-mark" width="44" height="36" viewBox="0 0 44 36" fill="#3158f0"><path d="M0 22C0 10 6 3 16 0l2 5c-5 2-8 6-8 10h8v21H0zM24 22C24 10 30 3 40 0l2 5c-5 2-8 6-8 10h8v21H24z"/></svg>
  <p class="abs quote-text">Rowan's description of his abilities was accurate. He is very capable and responsive. He worked very quickly and efficiently, cheerfully incorporating suggestions and revisions within a short time frame. I have no hesitation in recommending Rowan to anyone who needs mechanical engineering work, or calculations, done.</p>
  <p class="abs quote-name">Malcolm Harte<span>Client</span></p>
</section>

<section class="abs cta">
  <h2>Curious what else we do?</h2>
  <a href="#">See Here</a>
</section>

<footer class="abs footer">
  <span class="social" style="left:174px"></span>
  <span class="social" style="left:216px"></span>
  <span class="social" style="left:258px"></span>
  <div class="f-info" style="left:395px"><small>Email Address</small>info@valtrobuild.design</div>
  <div class="f-info" style="left:609px"><small>Phone Number</small>+44 (0)7700 900 318</div>
  <div class="f-info" style="left:803px"><small>Location</small>We're based in South Wales, UK.</div>
  <div class="f-bar">
    <span class="top">Back to top</span>
    <span class="copy">© Copyright 2025<br>Valtro Mechanical Design. All Right Reserved</span>
  </div>
  <div class="wordmark">valtro</div>
</footer>

</body>
</html>
```